Tri-fold discount dental plan brochure
We need a standard Tri-fold brochure for our discount dental membership plan. Attached is a Word documents which contains the text for the brochure.
Health
Please use the text that is provided in the word document attached. Also pictures can be used form pictovanta.com and we will purchase them later on.
logo
content and copy can be download here.
pleasse get the chart and application from these files

```html
<!DOCTYPE html>
<html lang="en">
<head>
<meta charset="utf-8">
<title>RQO Dental Plan – Tri-fold Brochure</title>
<link rel="stylesheet" href="https://fonts.googleapis.com/css2?family=Arimo:wght@400;700&family=Lora:wght@400&display=swap">
<style>
:root{
  --navy:#0d4f8f;
  --blue:#1a6bb3;
  --sky:#dbe8f5;
  --pale:#f2f6fb;
  --ink:#27333f;
  --grey:#8a96a3;
  --white:#ffffff;
  --bg:#ffffff;
  --photo-skin:#c9a88f;
  --photo-light:#e6eef6;
}
*{box-sizing:border-box;margin:0;padding:0}
html,body{width:1200px;height:689px;overflow:hidden;background:var(--bg)}
body{font-family:"Arimo",Arial,sans-serif;color:var(--ink);position:relative}
.spread{position:absolute;display:flex;box-shadow:0 4px 14px rgba(0,0,0,.25);background:var(--white)}
.spread--outside{left:30px;top:70px;width:510px;height:430px}
.spread--inside{left:560px;top:40px;width:620px;height:390px}
.panel{position:relative;flex:1;overflow:hidden;font-size:5.5px;line-height:1.45}
.panel + .panel{border-left:1px solid #d6dee8}
.photo{position:absolute;border-radius:6px}
.caption{position:absolute;font-family:"Lora",Georgia,serif;font-size:24px;color:#444}
.caption--outside{left:110px;top:555px}
.caption--inside{left:760px;top:455px}

/* outside spread */
.howitworks{background:var(--navy);color:var(--white);padding:14px 12px}
.howitworks h3{font-size:9px;text-align:center;margin-bottom:8px}
.howitworks ol{padding-left:10px}
.howitworks li{margin-bottom:8px}
.howitworks .footnote{position:absolute;left:12px;right:12px;bottom:14px}
.testimonials{background:var(--pale)}
.testimonials .quotes{position:absolute;left:12px;right:8px;top:120px;height:210px;background:var(--white);border:2px solid var(--blue);border-radius:10px;padding:10px}
.testimonials h3{color:var(--navy);font-size:8px;margin-bottom:8px}
.testimonials p{margin-bottom:8px}
.testimonials .name{color:var(--blue);text-align:right;font-style:italic}
.band{position:absolute;left:0;right:0;bottom:12px;height:22px;background:var(--blue);opacity:.8}
.cover .brand{position:absolute;top:28px;left:16px;display:flex;align-items:center;gap:6px;color:var(--navy);font-weight:700;font-size:15px;white-space:nowrap}
.brand .dot{width:12px;height:12px;border-radius:50%;background:var(--blue);flex:none}
.cover .tag{position:absolute;top:50px;left:34px;font-size:5px;color:var(--grey);white-space:nowrap}
.cover .call{position:absolute;left:0;right:0;top:270px;height:110px;background:var(--blue);color:var(--white);text-align:center;padding-top:18px;font-size:17px;line-height:1.25}
.cover .call strong{display:block;font-size:19px;margin-top:8px}

/* inside spread */
.hero{position:absolute;left:0;top:0;width:413px;height:112px;background:linear-gradient(90deg,var(--photo-light),var(--photo-skin) 70%,#9ab2cc)}
.intro{padding:120px 12px 0}
.intro .brand{display:flex;align-items:center;gap:5px;color:var(--navy);font-weight:700;font-size:10px;position:absolute;top:30px;left:40px;white-space:nowrap}
.intro h4{position:absolute;top:48px;left:40px;color:var(--navy);font-size:6px;font-weight:400}
.intro p{margin-bottom:6px}
.why{position:absolute;left:10px;right:10px;top:240px;background:var(--blue);color:var(--white);border-radius:8px;padding:8px}
.why h3{font-size:8px;margin-bottom:5px}
.savings{padding:120px 8px 0}
.savings h3{color:var(--navy);font-size:7px;margin-bottom:4px;text-align:center}
table{width:100%;border-collapse:collapse;font-size:5px}
th{background:var(--navy);color:var(--white);padding:2px;text-align:left}
td{padding:1.5px 2px;border-bottom:1px solid #d6dee8}
tr:nth-child(even) td{background:var(--sky)}
.application{padding:12px 10px}
.application h2{color:var(--navy);font-size:14px;margin-bottom:6px}
.field{display:flex;gap:4px;margin-bottom:6px;align-items:flex-end}
.field span{white-space:nowrap}
.field i{flex:1;border-bottom:1px solid var(--grey);height:6px}
.application h5{color:var(--navy);font-size:6px;margin:8px 0 5px}
.boxes{display:flex;gap:8px;margin-bottom:6px}
.boxes span::before{content:"";display:inline-block;width:5px;height:5px;border:1px solid var(--grey);margin-right:3px;vertical-align:middle}
</style>
</head>
<body>

<section class="spread spread--outside">
  <div class="panel howitworks">
    <h3>How Does It Work?</h3>
    <ol>
      <li>Enroll online or by phone and choose a plan that fits your family and your budget.</li>
      <li>Receive your member card and visit any participating dentist near your home.</li>
      <li>Show your card at each visit and pay the reduced member rate directly.</li>
      <li>Save on cleanings, fillings, crowns and more with no forms or waiting periods.</li>
    </ol>
    <div class="photo" role="img" aria-label="Photo of a smiling woman" style="left:12px;top:262px;width:146px;height:90px;background:linear-gradient(135deg,var(--photo-light),var(--photo-skin))"></div>
    <p class="footnote">This plan is not insurance. Members pay providers directly at the discounted rate.</p>
  </div>

  <div class="panel testimonials">
    <div class="photo" role="img" aria-label="Photo of a smiling family" style="left:12px;top:14px;width:146px;height:92px;background:linear-gradient(135deg,var(--photo-light),var(--photo-skin))"></div>
    <div class="quotes">
      <h3>What Our Customers Are Saying!</h3>
      <p>"We saved over $1,000 on our family's dental work this year."</p>
      <p class="name">– Member, Ohio</p>
      <p>"Signing up took minutes and my dentist was already on the list."</p>
      <p class="name">– Member, Texas</p>
      <p>"Simple, honest and affordable. I tell all my friends about it."</p>
      <p class="name">– Member, Florida</p>
    </div>
    <div class="photo" role="img" aria-label="Photo of a smiling young woman" style="left:50px;top:300px;width:80px;height:70px;background:linear-gradient(135deg,var(--photo-light),var(--photo-skin))"></div>
    <div class="band"></div>
  </div>

  <div class="panel cover">
    <div class="brand"><span class="dot"></span>RQO DentalPlan</div>
    <p class="tag">Affordable dental care for every family</p>
    <div class="photo" role="img" aria-label="Photo of a smiling man" style="left:12px;top:80px;width:146px;height:170px;background:linear-gradient(135deg,var(--photo-light),var(--photo-skin))"></div>
    <div class="call">Call RQO Dental<br>today on<strong>1.877.555.0142</strong></div>
    <div class="band"></div>
  </div>
</section>

<section class="spread spread--inside">
  <div class="hero" role="img" aria-label="Photo of a smiling family of four"></div>
  <div class="panel intro">
    <div class="brand"><span class="dot"></span>RQO DentalPlan</div>
    <h4>Discount Dental Benefits</h4>
    <p>The RQO Dental Plan is a discount membership that gives you reduced fees at thousands of participating dentists nationwide.</p>
    <p>There are no deductibles, no yearly limits and no claim forms. Your savings start as soon as your card arrives.</p>
    <div class="why">
      <h3>Why choose RQO Dental Plan?</h3>
      <p>Members save on average half of the usual fees for most routine and major dental services, with plans for individuals and families.</p>
    </div>
  </div>
  <div class="panel savings">
    <h3>Typical Dental Savings with your plan</h3>
    <table>
      <tr><th>Procedure</th><th>Usual</th><th>Member</th></tr>
      <tr><td>Exam</td><td>$60</td><td>$25</td></tr>
      <tr><td>Cleaning</td><td>$95</td><td>$45</td></tr>
      <tr><td>X-rays</td><td>$120</td><td>$50</td></tr>
      <tr><td>Filling</td><td>$150</td><td>$70</td></tr>
      <tr><td>Root canal</td><td>$900</td><td>$480</td></tr>
      <tr><td>Crown</td><td>$1,100</td><td>$590</td></tr>
      <tr><td>Extraction</td><td>$180</td><td>$85</td></tr>
      <tr><td>Denture</td><td>$1,400</td><td>$720</td></tr>
      <tr><td>Braces</td><td>$5,200</td><td>$3,600</td></tr>
      <tr><td>Whitening</td><td>$450</td><td>$220</td></tr>
    </table>
  </div>
  <div class="panel application">
    <h2>Application</h2>
    <div class="field"><span>Mail To:</span><i></i></div>
    <div class="field"><span>First Name</span><i></i></div>
    <div class="field"><span>Last Name</span><i></i></div>
    <div class="field"><span>Address</span><i></i></div>
    <div class="field"><span>City</span><i></i><span>State</span><i></i></div>
    <div class="field"><span>Phone</span><i></i></div>
    <div class="field"><span>Email</span><i></i></div>
    <h5>Additional Household Family Members</h5>
    <div class="field"><span>Name</span><i></i></div>
    <div class="field"><span>Name</span><i></i></div>
    <div class="field"><span>Name</span><i></i></div>
    <h5>Select Type of Membership</h5>
    <div class="boxes"><span>Individual</span><span>Couple</span><span>Family</span></div>
    <h5>Payment Type</h5>
    <div class="boxes"><span>Card</span><span>Check</span></div>
    <div class="field"><span>Signature</span><i></i></div>
  </div>
</section>

<p class="caption caption--outside">Front, back and folded panels</p>
<p class="caption caption--inside">Inside panels</p>

</body>
</html>
```